Art Business Needs a Wordpress Theme

I need a Wordpress theme for my company, Ve Ta Haven. Ve Ta stands for Love, Local and the company's focus is to increase awareness of local art and artists. The site will have a blog with posts that showcase local art, art how-to techniques, featured artists and art events. These could be broken down into separate pages or just kept within the homepage. I have a logo that I would like to incorporate. The only request I will make about the layout is that it can feature pictures prominently. Eventually with the help of a Fundrally campaign I would like to turn the site into an upscale e-commerce platform for member artists of the site. The blog that you are designing will be built on as the business grows into its full vision.

Target Market(s)

Young professionals, Art fans and home designers

Industry/Entity Type

Business

Number of Pages Required

3 page

Font styles to use
Sans Serif

Colors
eda3c7
e667a6
e34197
f59195
f04a50
f68d4d
f37122

Requirements
Must have
• An about page and a contact page. I would like it if the logo was featured on the top left of the screen along with the words Love. Local. Art.
Nice to have
• Perhaps if possible it would be cool to have a way for people to enter their email if they were interested in joining a mailing list or having the Social media information displayed on a sidebar.

```html
<!DOCTYPE html>
<html lang="en">
<head>
<meta charset="utf-8">
<title>Ve Ta Haven — Love. Local. Art.</title>
<link href="https://fonts.googleapis.com/css2?family=Open+Sans:wght@400;600;700&display=swap" rel="stylesheet">
<style>
:root{
  --pink:#e34197;
  --pink-mid:#e667a6;
  --pink-soft:#eda3c7;
  --orange:#f37122;
  --orange-soft:#f68d4d;
  --coral:#f04a50;
  --dark:#262626;
  --footer:#303030;
  --footer-deep:#222;
  --text:#444;
  --muted:#888;
  --line:#e2e2e2;
  --page:#ffffff;
}
*{box-sizing:border-box;margin:0;padding:0}
html,body{width:1200px;height:3064px;overflow:hidden}
body{font-family:"Open Sans",Arial,sans-serif;color:var(--text);background:var(--page);position:relative}

.site-header{position:absolute;top:0;left:0;width:1200px;height:144px;background:#fff}
.brand{position:absolute;left:40px;top:14px;width:110px;text-align:center}
.brand-mark{width:74px;height:74px;border-radius:50%;background:var(--pink);margin:0 auto 6px}
.brand-name{color:var(--pink);font-size:22px;font-weight:600;white-space:nowrap}
.search{position:absolute;left:300px;top:66px;display:flex}
.search-input{width:290px;height:34px;border:1px solid #ccc;font-size:12px;color:#999;padding:8px 10px}
.search-btn{width:110px;height:34px;background:var(--pink);color:#fff;font-size:12px;font-weight:700;display:flex;align-items:center;justify-content:center;margin-left:6px}
.member-note{position:absolute;left:840px;top:74px;font-size:13px;color:#666}
.btn-orange{background:var(--orange);color:#fff;font-weight:700;font-size:12px;display:flex;align-items:center;justify-content:center}
.login{position:absolute;left:1010px;top:66px;width:80px;height:34px}
.register{position:absolute;left:1104px;top:66px;width:84px;height:34px}

.main-nav{position:absolute;top:144px;left:0;width:1200px;height:40px;background:var(--dark);display:flex;padding-left:88px}
.main-nav a{color:#fff;font-size:12px;font-weight:700;text-decoration:none;line-height:40px;margin-right:64px}

.post{position:absolute;left:88px;width:692px}
.post-photo{width:692px;height:400px}
.photo-frame{background:linear-gradient(135deg,#d9d9d9,#7a7a7a 60%,#3a3a3a)}
.photo-spray{background:linear-gradient(120deg,#f1e7dc,#e8b48c 35%,#6d90b8 65%,#c24b3a)}
.photo-statue{background:linear-gradient(160deg,#b6ab91,#7d735d 55%,#4d4537)}
.post-title{font-size:28px;line-height:40px;font-weight:700;color:#222;margin-top:24px}
.post-meta{display:flex;align-items:center;font-size:12px;color:var(--muted);margin-top:14px;gap:14px}
.meta-icon{width:12px;height:12px;border-radius:2px;background:var(--pink);display:inline-block;margin-right:4px;vertical-align:-1px}
.share{display:flex;gap:6px}
.share span{width:22px;height:22px;border-radius:50%}
.post-body{margin-top:26px;font-size:13px;line-height:22px;color:#666}
.post-body p{margin-bottom:18px}

.load-more{position:absolute;left:214px;top:2640px;width:440px;height:40px;font-size:12px;border-radius:3px}

.sidebar{position:absolute;left:832px;top:220px;width:272px}
.about-photo{width:272px;height:180px;background:linear-gradient(140deg,#f3c9a0,#e46a8b 45%,#5a8fd1 80%)}
.about-title{font-size:14px;font-weight:700;color:#222;margin-top:18px}
.about-text{font-size:12px;line-height:19px;color:#777;margin-top:10px}
.widget{border:1px solid var(--line);margin-top:28px}
.widget-head{background:var(--pink);color:#fff;font-size:12px;font-weight:700;padding:10px 12px}
.widget-body{padding:14px 12px}
.follow-note{font-size:12px;color:#777;text-align:center}
.follow-icons{display:flex;justify-content:center;gap:8px;margin-top:12px;flex-wrap:wrap}
.follow-icons span{width:28px;height:28px;border-radius:50%}
.mini-list{list-style:none}
.mini-item{display:flex;gap:12px;padding:10px 0;border-bottom:1px solid #eee}
.mini-item:last-child{border-bottom:none}
.mini-thumb{width:80px;height:58px;flex:none}
.mini-title{font-size:12px;font-weight:700;color:#333;line-height:17px}
.mini-tag{font-size:11px;color:var(--muted);margin-top:4px}
.fl-card{border:1px solid #ddd;padding:10px}
.fl-top{display:flex;gap:10px;align-items:center}
.fl-avatar{width:46px;height:46px;background:var(--pink-soft)}
.fl-name{font-size:12px;font-weight:700;color:#333}
.fl-like{display:inline-block;margin-top:4px;font-size:10px;border:1px solid #ccc;padding:1px 6px;color:#555}
.fl-count{font-size:11px;color:#777;margin:10px 0 8px}
.fl-grid{display:grid;grid-template-columns:repeat(6,1fr);gap:6px}
.fl-grid span{height:36px;background:linear-gradient(135deg,#c9b8a8,#7d6c62)}
.fl-foot{font-size:10px;color:#999;margin-top:8px}
.news-note{font-size:12px;color:#777;line-height:18px}
.field{height:32px;border:1px solid #ccc;margin-top:10px;font-size:12px;color:#aaa;padding:7px 10px}
.subscribe{height:32px;margin-top:12px;width:130px;border-radius:2px}

.site-footer{position:absolute;top:2752px;left:0;width:1200px;height:312px;background:var(--footer)}
.footer-brand{position:absolute;left:88px;top:46px;width:110px;text-align:center}
.footer-col{position:absolute;top:50px;width:200px}
.footer-col h4{color:#fff;font-size:13px;font-weight:700;margin-bottom:12px}
.footer-col li{list-style:none;color:#aaa;font-size:12px;line-height:21px}
.footer-bar{position:absolute;left:0;bottom:0;width:1200px;height:44px;background:var(--footer-deep);color:#999;font-size:11px;text-align:center;line-height:44px}
.footer-top{position:absolute;right:88px;bottom:14px;width:16px;height:16px}
</style>
</head>
<body>

<header class="site-header">
  <div class="brand">
    <div class="brand-mark"></div>
    <div class="brand-name">Ve Ta Haven</div>
  </div>
  <div class="search">
    <div class="search-input">Enter your keyword</div>
    <div class="search-btn">SEARCH</div>
  </div>
  <div class="member-note">Become a Member above</div>
  <div class="btn-orange login">LOGIN</div>
  <div class="btn-orange register">REGISTER</div>
</header>

<nav class="main-nav">
  <a>HOME</a><a>ABOUT US</a><a>DESIGN</a><a>ARTISTS</a><a>INSPIRATION</a><a>ARTICLES</a>
</nav>

<article class="post" style="top:220px">
  <div class="post-photo photo-frame" role="img" aria-label="Black and white photo of a person framing their view with both hands"></div>
  <h2 class="post-title">Lorem Ipsum is simply dummy text of the printing and typesetting industry</h2>
  <div class="post-meta">
    <span>Posted On : 17 March 2015</span>
    <span><i class="meta-icon"></i>Ve Ta Haven</span>
    <span><i class="meta-icon"></i>(12) Comments</span>
    <div class="share"><span style="background:#3b5998"></span><span style="background:#29a9e1"></span><span style="background:#d6392b"></span><span style="background:#cb2027"></span><span style="background:#0e76a8"></span><span style="background:#e34197"></span></div>
  </div>
  <div class="post-body">
    <p>Lorem Ipsum is simply dummy text of the printing and typesetting industry. Lorem Ipsum has been the industry's standard dummy text ever since the 1500s, when an unknown printer took a galley of type and scrambled it to make a type specimen book. It has survived not only five centuries, but also the leap into electronic typesetting, remaining essentially unchanged.</p>
    <p>It was popularised in the 1960s with the release of Typeleaf sheets containing Lorem Ipsum passages, and more recently with desktop publishing software like Pressmark Layout including versions of Lorem Ipsum.</p>
  </div>
</article>

<article class="post" style="top:1020px">
  <div class="post-photo photo-spray" role="img" aria-label="Hand holding a spray paint can in front of a colourful mural"></div>
  <h2 class="post-title">Lorem Ipsum is simply dummy text of the printing and typesetting industry</h2>
  <div class="post-meta">
    <span>Posted On : 17 March 2015</span>
    <span><i class="meta-icon"></i>Ve Ta Haven</span>
    <span><i class="meta-icon"></i>(12) Comments</span>
    <div class="share"><span style="background:#3b5998"></span><span style="background:#29a9e1"></span><span style="background:#d6392b"></span><span style="background:#cb2027"></span><span style="background:#0e76a8"></span><span style="background:#e34197"></span></div>
  </div>
  <div class="post-body">
    <p>Lorem Ipsum is simply dummy text of the printing and typesetting industry. Lorem Ipsum has been the industry's standard dummy text ever since the 1500s, when an unknown printer took a galley of type and scrambled it to make a type specimen book. It has survived not only five centuries, but also the leap into electronic typesetting, remaining essentially unchanged.</p>
    <p>It was popularised in the 1960s with the release of Typeleaf sheets containing Lorem Ipsum passages, and more recently with desktop publishing software like Pressmark Layout including versions of Lorem Ipsum.</p>
  </div>
</article>

<article class="post" style="top:1840px">
  <div class="post-photo photo-statue" role="img" aria-label="Stone relief sculpture of a winged figure"></div>
  <h2 class="post-title">Lorem Ipsum is simply dummy text of the printing and typesetting industry</h2>
  <div class="post-meta">
    <span>Posted On : 17 March 2015</span>
    <span><i class="meta-icon"></i>Ve Ta Haven</span>
    <span><i class="meta-icon"></i>(12) Comments</span>
    <div class="share"><span style="background:#3b5998"></span><span style="background:#29a9e1"></span><span style="background:#d6392b"></span><span style="background:#cb2027"></span><span style="background:#0e76a8"></span><span style="background:#e34197"></span></div>
  </div>
  <div class="post-body">
    <p>Lorem Ipsum is simply dummy text of the printing and typesetting industry. Lorem Ipsum has been the industry's standard dummy text ever since the 1500s, when an unknown printer took a galley of type and scrambled it to make a type specimen book. It has survived not only five centuries, but also the leap into electronic typesetting, remaining essentially unchanged.</p>
    <p>It was popularised in the 1960s with the release of Typeleaf sheets containing Lorem Ipsum passages, and more recently with desktop publishing software like Pressmark Layout including versions of Lorem Ipsum.</p>
  </div>
</article>

<div class="btn-orange load-more">LOAD MORE POSTS</div>

<aside class="sidebar">
  <div class="about-photo" role="img" aria-label="Artist with colourful paint in a bright studio"></div>
  <h3 class="about-title">ABOUT VE TA HAVEN</h3>
  <p class="about-text">Lorem Ipsum is simply dummy text of the printing and typesetting industry. Lorem Ipsum has been the industry's standard dummy text ever since the 1500s.</p>

  <section class="widget">
    <div class="widget-head">FOLLOW US</div>
    <div class="widget-body">
      <p class="follow-note">Connect with us on social media</p>
      <div class="follow-icons">
        <span style="background:#3b5998"></span><span style="background:#29a9e1"></span><span style="background:#d6392b"></span><span style="background:#cb2027"></span><span style="background:#0e76a8"></span><span style="background:#f37122"></span><span style="background:#e34197"></span>
      </div>
    </div>
  </section>

  <section class="widget">
    <div class="widget-head">POPULAR POSTS</div>
    <div class="widget-body" style="padding-top:4px;padding-bottom:4px">
      <ul class="mini-list">
        <li class="mini-item"><div class="mini-thumb" style="background:linear-gradient(135deg,#7ab6e0,#2d5d8a)" role="img" aria-label="Tattoo artwork"></div><div><div class="mini-title">100+ Elegant Tattoo Designs</div><div class="mini-tag">Artwork</div></div></li>
        <li class="mini-item"><div class="mini-thumb" style="background:linear-gradient(135deg,#f59195,#b84c5a)" role="img" aria-label="Tattoo artwork"></div><div><div class="mini-title">100+ Elegant Tattoo Designs</div><div class="mini-tag">Artwork</div></div></li>
        <li class="mini-item"><div class="mini-thumb" style="background:linear-gradient(135deg,#9ccf8a,#3f7d4f)" role="img" aria-label="Tattoo artwork"></div><div><div class="mini-title">100+ Elegant Tattoo Designs</div><div class="mini-tag">Artwork</div></div></li>
        <li class="mini-item"><div class="mini-thumb" style="background:linear-gradient(135deg,#e8d3c0,#9a7a68)" role="img" aria-label="Tattoo artwork"></div><div><div class="mini-title">100+ Elegant Tattoo Designs</div><div class="mini-tag">Artwork</div></div></li>
      </ul>
    </div>
  </section>

  <section class="widget">
    <div class="widget-head">FRIENDLINK</div>
    <div class="widget-body">
      <div class="fl-card">
        <div class="fl-top"><div class="fl-avatar"></div><div><div class="fl-name">Ve Ta Haven</div><span class="fl-like">Like Page</span></div></div>
        <div class="fl-count">1,204 people like Ve Ta Haven</div>
        <div class="fl-grid" role="img" aria-label="Grid of follower thumbnails">
          <span></span><span></span><span></span><span></span><span></span><span></span>
          <span></span><span></span><span></span><span></span><span></span><span></span>
          <span></span><span></span><span></span><span></span><span></span><span></span>
        </div>
        <div class="fl-foot">Friendlink social plugin</div>
      </div>
    </div>
  </section>

  <section class="widget">
    <div class="widget-head">NEWSLETTER SIGNUP</div>
    <div class="widget-body">
      <p class="news-note">Get our stories updated through your email</p>
      <div class="field">Name</div>
      <div class="field">Email</div>
      <div class="btn-orange subscribe">SUBSCRIBE</div>
    </div>
  </section>

  <section class="widget">
    <div class="widget-head">ARTICLES</div>
    <div class="widget-body" style="padding-top:4px;padding-bottom:4px">
      <ul class="mini-list">
        <li class="mini-item"><div class="mini-thumb" style="background:linear-gradient(135deg,#7ab6e0,#2d5d8a)" role="img" aria-label="Tattoo artwork"></div><div><div class="mini-title">100+ Elegant Tattoo Designs</div><div class="mini-tag">Artwork</div></div></li>
        <li class="mini-item"><div class="mini-thumb" style="background:linear-gradient(135deg,#e9b66a,#a8662a)" role="img" aria-label="Tattoo artwork"></div><div><div class="mini-title">100+ Elegant Tattoo Designs</div><div class="mini-tag">Artwork</div></div></li>
        <li class="mini-item"><div class="mini-thumb" style="background:linear-gradient(135deg,#f59195,#b84c5a)" role="img" aria-label="Tattoo artwork"></div><div><div class="mini-title">100+ Elegant Tattoo Designs</div><div class="mini-tag">Artwork</div></div></li>
        <li class="mini-item"><div class="mini-thumb" style="background:linear-gradient(135deg,#f68d4d,#b04a1e)" role="img" aria-label="Tattoo artwork"></div><div><div class="mini-title">100+ Elegant Tattoo Designs</div><div class="mini-tag">Artwork</div></div></li>
        <li class="mini-item"><div class="mini-thumb" style="background:linear-gradient(135deg,#d9d27a,#8a8a3a)" role="img" aria-label="Tattoo artwork"></div><div><div class="mini-title">100+ Elegant Tattoo Designs</div><div class="mini-tag">Artwork</div></div></li>
        <li class="mini-item"><div class="mini-thumb" style="background:linear-gradient(135deg,#9ccf8a,#3f7d4f)" role="img" aria-label="Tattoo artwork"></div><div><div class="mini-title">100+ Elegant Tattoo Designs</div><div class="mini-tag">Artwork</div></div></li>
        <li class="mini-item"><div class="mini-thumb" style="background:linear-gradient(135deg,#e8d3c0,#9a7a68)" role="img" aria-label="Tattoo artwork"></div><div><div class="mini-title">100+ Elegant Tattoo Designs</div><div class="mini-tag">Artwork</div></div></li>
      </ul>
    </div>
  </section>
</aside>

<footer class="site-footer">
  <div class="footer-brand">
    <div class="brand-mark"></div>
    <div class="brand-name">Ve Ta Haven</div>
  </div>
  <div class="footer-col" style="left:296px">
    <h4>WELCOME</h4>
    <ul><li>About</li><li>Advertise</li><li>Contact</li><li>Submit Tips</li><li>Authors</li><li>Write for us</li><li>Publishing</li></ul>
  </div>
  <div class="footer-col" style="left:500px">
    <h4>INFORMATION</h4>
    <ul><li>Terms &amp; Conditions</li><li>Privacy Policy</li><li>Disclaimer</li><li>Sitemap</li></ul>
  </div>
  <div class="footer-col" style="left:700px">
    <h4>RELATED LINKS</h4>
    <ul><li>Lorem ipsum is simply dummy</li><li>Lorem ipsum is simply text</li><li>Lorem ipsum is simply dummy</li><li>Lorem ipsum is simply</li><li>Lorem ipsum is simply</li><li>Lorem ipsum is simply dummy</li></ul>
  </div>
  <div class="footer-col" style="left:920px">
    <h4>RELATED TOPICS</h4>
    <ul><li>Lorem ipsum is simply dummy</li><li>Lorem ipsum is simply</li><li>Lorem ipsum is simply dummy</li><li>Lorem ipsum is simply text</li><li>Lorem ipsum is simply</li><li>Lorem ipsum is simply dummy</li></ul>
  </div>
  <div class="footer-bar">© Copyright 2015, Ve Ta Haven. All Rights Reserved.</div>
  <svg class="footer-top" viewBox="0 0 16 16" aria-hidden="true"><path d="M3 11 L8 5 L13 11" fill="none" stroke="#999" stroke-width="2"/></svg>
</footer>

</body>
</html>
```